Package Design - Disposable Face Towel

Hi,

We are needing assistance with graphic design on our box/carton/package.

The attached image that is white is our biggest competitor.

Our brand is "BRIGHT DEW LTD." Please see the logo we uploaded.

Oder we have in mind for front of box:

Logo
LARGE TOWELS
50 Count
Ultra Soft| 100% USDA Bio-Based|100% Eucalyptus Viscose | Vegan
BRIGHTDEWLTD.EXAMPLE

We like medium to dark blue on most of the box, with white and minimal hot pink or salmon. Something that is sharp, modern, and stands out from our competitors.

Box dimensions are: 6.25 x 5.25 x 4.75 inches

This will be 1 of many design projects.

Target Market(s)

Female Beauty Products

Font styles to use
Serif
Sans Serif

Colors
0054AA
0677BA
7BADD7
CADEEF
E8F1F8
EB3D1F
EC4F4E
F09395
F8D3D4
FCEDEE

Requirements
Must have
• Needs to look sharp and modern

```html
<!DOCTYPE html>
<html lang="en">
<head>
<meta charset="utf-8">
<title>Bright Dew Ltd. – XL Soft Cloths Carton</title>
<link href="https://fonts.googleapis.com/css2?family=Poppins:wght@300;400;600;700&family=Oswald:wght@500&display=swap" rel="stylesheet">
<style>
  :root{
    --navy:#14285a;
    --navy-deep:#0f2150;
    --navy-soft:#223a72;
    --panel-grey:#ececec;
    --band-white:#f2f2f2;
    --ink:#1a2b55;
    --white:#ffffff;
    --gold-a:#d9b64a;
    --gold-b:#f4d671;
    --gold-c:#b8892a;
    --coral:#e0393f;
    --perf:#c0283a;
    --bg:#e6e6e6;
  }
  *{box-sizing:border-box;margin:0;padding:0}
  html,body{width:1200px;height:900px;overflow:hidden;background:var(--bg);font-family:"Poppins",sans-serif}
  .stage{width:1200px;height:900px;display:flex;justify-content:center;align-items:center;gap:60px}
  .carton{display:grid;grid-template-columns:200px 340px;grid-template-rows:120px 440px}
  .top-flap{grid-column:1 / 3;grid-row:1;background:linear-gradient(160deg,var(--navy-soft),var(--navy));display:flex;justify-content:center;align-items:flex-start;padding-top:26px;padding-left:120px}
  .flap-pill{font-size:11px;font-weight:700;letter-spacing:1px;padding:4px 22px;border-radius:20px;white-space:nowrap}
  .side-panel{grid-column:1;grid-row:2;background:var(--panel-grey);position:relative;padding:40px 18px 0 20px;color:var(--ink)}
  .side-title{font-family:"Oswald",sans-serif;font-weight:500;font-size:19px;letter-spacing:-.3px;margin-bottom:8px}
  .side-copy{font-size:9.6px;line-height:1.55;font-weight:400}
  .side-band{position:absolute;left:0;right:0;bottom:60px;height:44px;background:var(--navy)}
  .side-base{position:absolute;left:0;right:0;bottom:0;height:60px;background:var(--band-white)}
  .front-panel{grid-column:2;grid-row:2;position:relative;color:var(--white)}
  .front-art{position:absolute;inset:0 0 60px 0;background:radial-gradient(circle at 60% 30%,var(--navy-soft),var(--navy) 65%)}
  .perforation{position:absolute;left:0;top:0;width:340px;height:380px}
  .brand{position:absolute;top:82px;left:0;right:0;text-align:center;font-weight:300;font-size:25px;letter-spacing:2px}
  .product-pill{position:absolute;top:234px;left:50%;transform:translateX(-50%);white-space:nowrap;font-weight:700;font-size:21px;padding:7px 24px;border-radius:30px}
  .features{position:absolute;top:288px;left:0;right:0;text-align:center;font-size:11.5px;font-weight:300;line-height:1.7;letter-spacing:.3px}
  .count{position:absolute;top:334px;left:0;right:0;text-align:center;font-size:12.5px;font-weight:600}
  .front-base{position:absolute;left:0;right:0;bottom:0;height:60px;background:var(--band-white);display:flex;justify-content:center;align-items:center}
  .web{color:var(--ink);font-size:11.5px;font-weight:700;letter-spacing:1.6px}
  .gold .flap-pill,.gold .product-pill{background:linear-gradient(90deg,var(--gold-a),var(--gold-b) 45%,var(--gold-c));color:var(--navy-deep)}
  .coral .flap-pill,.coral .product-pill{background:var(--coral);color:var(--white)}
</style>
</head>
<body>
<main class="stage">
  <section class="carton gold">
    <div class="top-flap" role="img" aria-label="Navy eucalyptus leaf pattern"><span class="flap-pill">XL SOFT CLOTHS</span></div>
    <div class="side-panel">
      <h2 class="side-title">XL SOFT CLOTHS</h2>
      <p class="side-copy">Lorem ipsum dolor sit amet, consectetur adipiscing elit. Nullam sollicitudin pellentesque nulla, convallis commodo erat euismod eget. Cras nec euismod orci, in ornare ante. Lorem ipsum dolor sit amet, consectetur adipiscing elit. Pellentesque in elementum urna. Donec elementum eu dolor vel tincidunt. Nulla sit amet molestie mi. Duis tempor dignissim erat in ultrices.</p>
      <div class="side-band"></div>
      <div class="side-base"></div>
    </div>
    <div class="front-panel">
      <div class="front-art" role="img" aria-label="Navy eucalyptus leaf pattern"></div>
      <svg class="perforation" viewBox="0 0 340 380" fill="none" stroke="var(--perf)" stroke-width="1" stroke-dasharray="3 3">
        <path d="M40 0 V170 H150 L160 182 H190 L200 170 H320 V0"/>
        <path d="M20 196 Q8 210 20 222 L320 200 Q332 186 320 176"/>
      </svg>
      <div class="brand">BRIGHT DEW LTD.</div>
      <div class="product-pill">XL SOFT CLOTHS</div>
      <div class="features">ULTRA SOFT &nbsp;|&nbsp; 100% USDA BIO-BASED<br>100% EUCALYPTUS VISCOSE &nbsp;|&nbsp; VEGAN</div>
      <div class="count">50 COUNT</div>
      <div class="front-base"><span class="web">BRIGHTDEWLTD.EXAMPLE</span></div>
    </div>
  </section>

  <section class="carton coral">
    <div class="top-flap" role="img" aria-label="Navy eucalyptus leaf pattern"><span class="flap-pill">XL SOFT CLOTHS</span></div>
    <div class="side-panel">
      <h2 class="side-title">XL SOFT CLOTHS</h2>
      <p class="side-copy">Lorem ipsum dolor sit amet, consectetur adipiscing elit. Nullam sollicitudin pellentesque nulla, convallis commodo erat euismod eget. Cras nec euismod orci, in ornare ante. Lorem ipsum dolor sit amet, consectetur adipiscing elit. Pellentesque in elementum urna. Donec elementum eu dolor vel tincidunt. Nulla sit amet molestie mi. Duis tempor dignissim erat in ultrices.</p>
      <div class="side-band"></div>
      <div class="side-base"></div>
    </div>
    <div class="front-panel">
      <div class="front-art" role="img" aria-label="Navy eucalyptus leaf pattern"></div>
      <svg class="perforation" viewBox="0 0 340 380" fill="none" stroke="var(--perf)" stroke-width="1" stroke-dasharray="3 3">
        <path d="M40 0 V170 H150 L160 182 H190 L200 170 H320 V0"/>
        <path d="M20 196 Q8 210 20 222 L320 200 Q332 186 320 176"/>
      </svg>
      <div class="brand">BRIGHT DEW LTD.</div>
      <div class="product-pill">XL SOFT CLOTHS</div>
      <div class="features">ULTRA SOFT &nbsp;|&nbsp; 100% USDA BIO-BASED<br>100% EUCALYPTUS VISCOSE &nbsp;|&nbsp; VEGAN</div>
      <div class="count">50 COUNT</div>
      <div class="front-base"><span class="web">BRIGHTDEWLTD.EXAMPLE</span></div>
    </div>
  </section>
</main>
</body>
</html>
```